NEW site with a tech flair and a feeling of moving forward!!

Hello Everyone,

We are starting with a small project to get the first 3-4 pages done. The winning designer will have an opportunity to work with us to design out the rest of the site. We estimate there will be between 15 and 20 total pages for the site (so there would probably be more work for the winner)!

We need a new website design to enhance the "coolness" factor of our brand image! Our current website is www.quillanmailworks.com and it needs some updating!

We envision a website where the homepage would be almost a landing page. It might have a 60 second video at the top, or a picture slider and contact info/site map at the bottom. In the middle we envision having the 3 service logos along with a quick summary of each service!

We have 3 main services: Tally Up, Shape Up and Send Off. We want to replace those names with our new service names which are: qUrgent, qPromoNet and qBlend-Up. Each service has its own unique logo! :)

If you look at www.quillanmailworks.com and notice the Tally Up / Shape Up / Send Off - - basically we are replacing those names with qUrgent / qPromoNet / and qBlend-Up. Then we just want to freshen things up - for example, the current information listed under "Tally Up" is "good" ...it just doesn't look "cool" ... we need a better way to display it. We provide complex services (and a lot of different services) and are hoping to make a new website that has a feel of being clean, modern, professional, with a technology flair and easy to use/understand our services.

The person visiting the website could watch the 60 second video to get an overview and then click on a logo for their desired service to be able to learn more. Once the user clicks a logo for the desired service, a new page would open and the user could then learn about the service.

After submitting a design for the homepage, please work on a design to totally revamp the "Tally Up" page. We don't like the way that is laid out and need to freshen it up. Note: the layout we choose for Tally Up will be similar for Send Off and Shape Up.

The perfect website will have a combo of a technology flair, a feeling of moving forward and/or of connecting people/things/information together. The website should convey trust.

ABOUT QUILLAN MAILWORKS

We are a technology and communications company. We receive data files, print, fold, insert and mail invoices, statements and other important notices. We also deliver via email, SMS/Text Message and IVR Phone calls. Finally we offer an online website where customers can go to pay their invoices. It is important that the website have a clean, modern, professional and technology look/feel.

We also provide marketing and advertising services through the mail and digitally.

**Please note, our main company is called Quillan Mailworks...we have uploaded our 2 new logos (for your reference) for qUrgent and qPromoNet for reference.

Please message me with any questions! Thanks everyone, looking forward to seeing the designs!

Target Market(s)

Financial companies, Healthcare and Utilities.

Industry/Entity Type

Tech

Number of Pages Required

5+ page

Requirements
Must have
• The perfect website will have a combo of a technology flair, a feeling of moving forward and/or of connecting people/things/information together. The website should convey trust.
Nice to have
• Taking our complicated services and products and making them really simple and easy to understand by using graphs, charts, pictures and other illustrations.
• Eye catchy feel. Needs to be simple. Conveys trustworthy feel.
Should not have
• Can't be boring and bland. Can't be too complex.

```html
<!DOCTYPE html>
<html lang="en">
<head>
<meta charset="utf-8">
<title>Quillan Mailworks</title>
<link href="https://fonts.googleapis.com/css2?family=Open+Sans:wght@400;600;700&family=Raleway:wght@300;400;600&display=swap" rel="stylesheet">
<style>
  :root{
    --navy:#17355f;
    --navy-deep:#0f2444;
    --accent:#1f9ad6;
    --accent-soft:#58b9e6;
    --text:#3c4450;
    --muted:#8d949c;
    --line:#e3e7eb;
    --footer:#ebedef;
    --white:#ffffff;
  }
  *{box-sizing:border-box;margin:0;padding:0}
  html,body{width:835px;height:1200px;overflow:hidden;background:var(--white)}
  body{font-family:"Open Sans",Arial,sans-serif;color:var(--text);position:relative}

  .top-bar{height:22px;background:var(--navy);display:flex;align-items:center;justify-content:space-between;padding:0 70px 0 68px;color:var(--white);font-size:8px}
  .top-bar .welcome{letter-spacing:.5px;font-weight:600}
  .top-bar .contact{display:flex;align-items:center;gap:14px}
  .top-bar .contact span{display:flex;align-items:center;gap:4px}
  .top-social{display:flex;gap:3px}
  .top-social i{width:11px;height:11px;border-radius:50%;background:var(--white);display:block}

  .site-header{height:75px;display:flex;align-items:center;justify-content:space-between;padding:0 70px 0 68px;background:var(--white);border-bottom:1px solid var(--line)}
  .brand{display:flex;align-items:center;gap:7px;font-family:"Raleway",sans-serif;font-size:19px;font-weight:400;color:var(--navy)}
  .brand .mark{width:12px;height:12px;background:var(--accent)}
  .main-nav{display:flex;align-items:center;gap:20px;font-size:8px;font-weight:600;color:var(--text);letter-spacing:.4px}
  .main-nav .active{color:var(--accent)}

  .hero{position:relative;height:363px;background:radial-gradient(ellipse at 72% 45%,#2f6aa3 0%,#1c4675 35%,var(--navy-deep) 75%);overflow:hidden}
  .hero-title{position:absolute;left:120px;top:108px;font-family:"Raleway",sans-serif;font-weight:300;font-size:30px;color:var(--white)}
  .play{position:absolute;left:170px;top:162px;width:36px;height:36px}
  .hero-wave{position:absolute;left:0;bottom:0;width:835px;height:70px}

  .services{position:absolute;left:0;top:480px;width:835px}
  .service-row{display:flex;justify-content:center;gap:22px;height:285px}
  .service{width:200px;text-align:center}
  .diamond-wrap{height:165px;display:flex;align-items:center;justify-content:center}
  .diamond{width:80px;height:80px;border:2px solid var(--line);border-radius:14px;transform:rotate(45deg);background:var(--white);box-shadow:0 6px 18px rgba(23,53,95,.12);display:flex;align-items:center;justify-content:center}
  .diamond svg{transform:rotate(-45deg);width:40px;height:40px}
  .service h3{font-size:13px;font-weight:600;color:var(--text);margin-top:52px;margin-bottom:10px}
  .service p{font-size:7.5px;line-height:11px;color:var(--muted);padding:0 4px}
  .read-more{display:inline-block;margin-top:7px;font-size:8.5px;color:var(--text)}
  .read-more b{color:var(--accent);font-weight:600}

  .site-footer{position:absolute;left:0;top:1085px;width:835px;height:115px;background:var(--footer);text-align:center}
  .footer-social{display:flex;justify-content:center;gap:7px;margin-top:20px}
  .footer-social i{width:17px;height:17px;border-radius:50%;background:#5e646b;display:block}
  .footer-nav{display:flex;justify-content:center;gap:16px;margin-top:15px;font-size:7px;font-weight:600;color:var(--text);letter-spacing:.3px}
  .copyright{font-size:7px;color:var(--muted);margin-top:12px}
  .to-top{position:absolute;right:60px;top:52px;font-size:8px;color:var(--muted)}
</style>
</head>
<body>

<div class="top-bar">
  <div class="welcome">WELCOME ▾</div>
  <div class="contact">
    <span>
      <svg width="8" height="8" viewBox="0 0 24 24"><path fill="#fff" d="M6.6 10.8a15 15 0 0 0 6.6 6.6l2.2-2.2c.3-.3.7-.4 1-.2 1.1.4 2.3.6 3.6.6.6 0 1 .4 1 1V20c0 .6-.4 1-1 1A17 17 0 0 1 3 4c0-.6.4-1 1-1h3.5c.6 0 1 .4 1 1 0 1.3.2 2.5.6 3.6.1.3 0 .7-.2 1z"/></svg>
      800-555-0142
    </span>
    <span>
      <svg width="8" height="8" viewBox="0 0 24 24"><path fill="#fff" d="M2 5h20v14H2z M2 5l10 8 10-8" stroke="#17355f" stroke-width="1.5"/></svg>
      hello@quillanmailworks.com
    </span>
    <div class="top-social"><i></i><i></i><i></i><i></i><i></i></div>
  </div>
</div>

<header class="site-header">
  <div class="brand"><span class="mark"></span>Quillan Mailworks</div>
  <nav class="main-nav">
    <span class="active">HOME</span><span>ABOUT US</span><span>SERVICES</span><span>PAY BILLS</span><span>SECURITY</span><span>CAREERS</span>
    <svg width="10" height="10" viewBox="0 0 24 24"><circle cx="10" cy="10" r="6" fill="none" stroke="#3c4450" stroke-width="2.5"/><path d="M15 15l6 6" stroke="#3c4450" stroke-width="2.5"/></svg>
  </nav>
</header>

<section class="hero" role="img" aria-label="Photo of a businessman holding a glowing smartphone security icon between his hands">
  <h1 class="hero-title">qUrgent</h1>
  <svg class="play" viewBox="0 0 36 36"><circle cx="18" cy="18" r="16" fill="none" stroke="#fff" stroke-width="2.5"/><path d="M14 11l11 7-11 7z" fill="#fff"/></svg>
  <svg class="hero-wave" viewBox="0 0 835 70" preserveAspectRatio="none"><path d="M0 70 L0 20 Q417 95 835 20 L835 70 Z" fill="#fff"/></svg>
</section>

<main class="services">
  <div class="service-row">
    <article class="service">
      <div class="diamond-wrap"><div class="diamond">
        <svg viewBox="0 0 40 40"><rect x="9" y="18" width="22" height="17" rx="2" fill="var(--accent)"/><path d="M14 18v-6a6 6 0 0 1 12-1" fill="none" stroke="var(--accent)" stroke-width="3"/><circle cx="20" cy="26" r="2.5" fill="#fff"/></svg>
      </div></div>
      <h3>Security</h3>
      <p>Your files travel through locked systems with tight access rules, so every notice and statement stays private from intake to delivery.</p>
      <span class="read-more">Read More <b>›</b></span>
    </article>
    <article class="service">
      <div class="diamond-wrap"><div class="diamond">
        <svg viewBox="0 0 40 40"><rect x="6" y="10" width="28" height="20" rx="2" fill="none" stroke="var(--accent)" stroke-width="2.5"/><rect x="6" y="15" width="28" height="4" fill="var(--accent)"/><rect x="10" y="23" width="8" height="2.5" fill="var(--accent)"/></svg>
      </div></div>
      <h3>Payment Processing</h3>
      <p>Customers pay invoices online at any hour through a simple portal, and each payment posts quickly to keep your accounts current.</p>
      <span class="read-more">Read More <b>›</b></span>
    </article>
    <article class="service">
      <div class="diamond-wrap"><div class="diamond">
        <svg viewBox="0 0 40 40"><rect x="4" y="12" width="20" height="15" fill="var(--accent)"/><path d="M24 16h7l5 6v5H24z" fill="var(--accent)"/><circle cx="11" cy="29" r="3.5" fill="var(--accent)" stroke="#fff" stroke-width="1.5"/><circle cx="30" cy="29" r="3.5" fill="var(--accent)" stroke="#fff" stroke-width="1.5"/></svg>
      </div></div>
      <h3>Omni-Channel Delivery</h3>
      <p>Reach people by mail, email, text message or phone call, all sent from one file and tracked together in a single clear report.</p>
      <span class="read-more">Read More <b>›</b></span>
    </article>
  </div>
  <div class="service-row">
    <article class="service">
      <div class="diamond-wrap"><div class="diamond">
        <svg viewBox="0 0 40 40"><rect x="15" y="5" width="10" height="8" fill="var(--accent)"/><rect x="4" y="27" width="10" height="8" fill="var(--accent)"/><rect x="15" y="27" width="10" height="8" fill="var(--accent)"/><rect x="26" y="27" width="10" height="8" fill="var(--accent)"/><path d="M20 13v8M9 27v-6h22v6M20 21v6" fill="none" stroke="var(--accent)" stroke-width="2"/></svg>
      </div></div>
      <h3>Mailpiece Integrity</h3>
      <p>Camera checks confirm each page lands in the right envelope, so every piece arrives complete, accurate and ready to be read.</p>
      <span class="read-more">Read More <b>›</b></span>
    </article>
    <article class="service">
      <div class="diamond-wrap"><div class="diamond">
        <svg viewBox="0 0 40 40"><rect x="9" y="10" width="22" height="15" rx="1.5" fill="none" stroke="var(--accent)" stroke-width="2.5"/><path d="M4 29h32l-3 3H7z" fill="var(--accent)"/></svg>
      </div></div>
      <h3>Self Service &amp; Single Sign...</h3>
      <p>One login opens every tool you need, letting your team send jobs, view proofs and pull reports without waiting on a call.</p>
      <span class="read-more">Read More <b>›</b></span>
    </article>
    <article class="service">
      <div class="diamond-wrap"><div class="diamond">
        <svg viewBox="0 0 40 40"><path d="M18 8a13 13 0 1 0 13 13H18z" fill="var(--accent)"/><path d="M21 5v13h13A13 13 0 0 0 21 5z" fill="var(--accent-soft)"/></svg>
      </div></div>
      <h3>Campaign Management</h3>
      <p>Plan, launch and measure print and digital campaigns in one place, with simple charts that show what your audience responds to.</p>
      <span class="read-more">Read More <b>›</b></span>
    </article>
  </div>
</main>

<footer class="site-footer">
  <div class="footer-social"><i></i><i></i><i></i><i></i><i></i></div>
  <nav class="footer-nav">
    <span>HOME</span><span>|</span><span>ABOUT US</span><span>|</span><span>SECURITY</span><span>|</span><span>INDUSTRIES</span><span>|</span><span>CAREERS</span><span>|</span><span>CONTACT US</span>
  </nav>
  <p class="copyright">2016 © Copyright Quillan Mailworks Inc. All Rights Reserved</p>
  <span class="to-top">▲</span>
</footer>

</body>
</html>
```